Geothermal company needs a creative "POW" business card

Manufacturers tend to be boring. We are not! We are a Geothermal Heat Pump company that has over 30 yrs of experience and wants a new look and updated feel. Nothing old (yawn) so get your creative hats on and let's rock!

We want to use the great colors of lime green and navy blue. Our new logo is attached and we're ready to roll. Remember, we're a professional leader in the geothermal industry that needs to make an eye catching and memorable first glance.

```html
<!DOCTYPE html>
<html lang="en">
<head>
<meta charset="utf-8">
<title>Boreal Loop – Business Card</title>
<link rel="stylesheet" href="https://fonts.googleapis.com/css2?family=Signika:wght@300;400;600&family=Roboto+Condensed:wght@400&display=swap">
<style>
  :root {
    --lime: #8dc63f;
    --navy: #002a5c;
    --white: #ffffff;
    --backdrop: #efefef;
  }
  * { margin: 0; padding: 0; box-sizing: border-box; }
  html, body {
    width: 1200px; height: 1000px; overflow: hidden;
    background: var(--backdrop);
    font-family: "Signika", sans-serif;
  }
  .card {
    position: absolute; top: 360px; width: 496px; height: 279px;
    overflow: hidden; background: var(--white);
    box-shadow: 0 12px 30px rgba(0,0,0,0.12);
  }
  .card--front { left: 67px; border-top-left-radius: 56px; }
  .card--back  { left: 639px; border-top-right-radius: 56px; }
  .card__band {
    position: absolute; left: 0; right: 0; top: 139px; bottom: 0;
  }
  .card--front .card__band { background: var(--lime); }
  .card--back .card__band  { background: var(--navy); }

  .brand-dot {
    position: absolute; border-radius: 50%; background: var(--navy);
  }
  .card--front .brand-dot { left: 31px; top: 29px; width: 82px; height: 82px; }
  .card--back .brand-dot  { left: 29px; top: 37px; width: 70px; height: 70px; }

  .brand-name {
    position: absolute; color: var(--lime); font-weight: 600;
    letter-spacing: -0.5px; line-height: 1; white-space: nowrap;
  }
  .card--front .brand-name { left: 133px; top: 40px; font-size: 50px; }
  .card--back .brand-name  { left: 117px; top: 50px; font-size: 42px; }

  .tagline {
    position: absolute; left: 135px; top: 88px;
    font-family: "Roboto Condensed", sans-serif; font-size: 13.5px;
    color: var(--navy); white-space: nowrap;
  }

  .person { position: absolute; left: 31px; top: 20px; }
  .person__name { font-size: 21px; font-weight: 600; color: var(--navy); line-height: 1.1; }
  .person__role { font-size: 19px; font-weight: 300; color: var(--white); line-height: 1.1; margin-top: 3px; }

  .contact {
    position: absolute; right: 29px; top: 46px;
    text-align: right; color: var(--white); font-size: 16px; font-weight: 300; line-height: 20.5px;
  }
  .address {
    position: absolute; left: 31px; top: 55px;
    color: var(--white); font-size: 16px; font-weight: 300; line-height: 20px;
  }
</style>
</head>
<body>
  <section class="card card--front">
    <span class="brand-dot"></span>
    <div class="brand-name">Boreal Loop</div>
    <div class="tagline">Makers of Ground-Source Heat Pumps for Cold Climates</div>
    <div class="card__band">
      <div class="person">
        <div class="person__name">Rhett Calloway</div>
        <div class="person__role">CEO</div>
      </div>
      <div class="contact">
        <div>p: (555) 014-2200</div>
        <div>f: (555) 014-2201</div>
        <div>e: rcalloway@borealloop.com</div>
      </div>
    </div>
  </section>

  <section class="card card--back">
    <span class="brand-dot"></span>
    <div class="brand-name">BorealLoop.com</div>
    <div class="card__band">
      <div class="address">
        <div>412 Cedar Ridge Rd</div>
        <div>Halvorsen, MN 56999</div>
      </div>
    </div>
  </section>
</body>
</html>
```